Website Header Development

I am after a redesign of the Header of a website www.kaltroweb.com.au.
This project is for the header only, and should fit in with the rest of the site
Target Market(s)
Business
Requirements
Should not have
- Over the top. Keep it simple

```html
<!DOCTYPE html>
<html lang="en">
<head>
<meta charset="utf-8">
<title>Kaltro Energy – Resource Efficiency</title>
<link rel="stylesheet" href="https://fonts.googleapis.com/css2?family=Alegreya:wght@500;700&family=Alegreya+Sans:wght@400;700&family=Open+Sans:wght@400&display=swap">
<style>
  :root {
    --navy: #0b1f86;
    --brand-blue: #1d3f94;
    --sidebar-blue: #21409a;
    --brand-green: #2a8a3e;
    --nav-green: #2b8a3f;
    --nav-green-dark: #167a3b;
    --grey-light: #f1f1f1;
    --grey-mid: #c9c9c9;
    --text: #1a1a1a;
    --field-border: #b5b5b5;
    --white: #ffffff;
  }
  * { margin: 0; padding: 0; box-sizing: border-box; }
  html, body { width: 1200px; height: 673px; overflow: hidden; background: var(--white); }
  body { position: relative; font-family: "Alegreya Sans", sans-serif; color: var(--text); }

  .site-header { position: absolute; left: 20px; top: 0; width: 1160px; height: 133px; }
  .header-art { position: absolute; inset: 0; }
  .brand {
    position: absolute; left: 65px; top: 54px;
    font-family: "Alegreya Sans", sans-serif; font-weight: 700; font-size: 37px;
    color: var(--brand-blue); letter-spacing: -0.5px; display: flex; align-items: center; gap: 12px;
  }
  .brand-mark { width: 20px; height: 20px; background: var(--brand-green); border-radius: 50%; }

  .main-nav {
    position: absolute; left: 20px; top: 133px; width: 1160px; height: 61px;
    background: linear-gradient(90deg, var(--nav-green) 0 1045px, var(--nav-green-dark) 1045px);
    overflow: hidden;
  }
  .main-nav::after {
    content: ""; position: absolute; left: 1045px; top: 0; width: 60px; height: 61px;
    background: var(--nav-green); transform-origin: top left; transform: skewX(45deg);
  }
  .main-nav a {
    position: absolute; color: var(--white); text-decoration: none; white-space: nowrap;
    font-family: "Alegreya Sans", sans-serif; font-size: 14px; top: 14px; z-index: 1;
  }
  .main-nav a.major { font-size: 17px; font-weight: 700; top: 20px; }

  .page-title {
    position: absolute; left: 89px; width: 680px; top: 230px; text-align: center;
    font-family: "Alegreya", serif; font-weight: 700; font-size: 28px; color: var(--navy);
  }
  .intro p {
    position: absolute; left: 89px; font-size: 16px; line-height: 29px;
  }
  .feature-photo {
    position: absolute; left: 354px; top: 302px; width: 406px; height: 270px;
    background: linear-gradient(110deg, #e9ecef 0%, #d6d2cd 45%, #b9b3ad 70%, #e7e9eb 100%);
  }

  .sidebar { position: absolute; left: 874px; top: 196px; width: 215px; }
  .search {
    width: 215px; height: 35px; border: 1px solid #d2d2d2; display: flex; align-items: center;
    padding-left: 9px; gap: 8px; font-family: "Open Sans", sans-serif; font-size: 15px; color: #8a8a8a;
  }
  .newsletter-title {
    margin-top: 40px; font-family: "Alegreya", serif; font-weight: 700; font-size: 23px;
    line-height: 35px; letter-spacing: 2px; color: var(--sidebar-blue);
  }
  .newsletter-copy { margin-top: 14px; font-size: 11.5px; font-weight: 700; line-height: 29px; }
  .field { width: 212px; height: 38px; border: 1px solid var(--field-border); margin: 8px 0 14px; }
</style>
</head>
<body>
  <header class="site-header">
    <svg class="header-art" width="1160" height="133" viewBox="0 0 1160 133">
      <defs>
        <linearGradient id="panelGrey" x1="0" y1="0" x2="0" y2="1">
          <stop offset="0" stop-color="#a8a8a8"/>
          <stop offset="0.12" stop-color="var(--grey-light)"/>
          <stop offset="0.8" stop-color="#e4e4e4"/>
          <stop offset="1" stop-color="#8c8c8c"/>
        </linearGradient>
      </defs>
      <rect width="1160" height="133" fill="var(--brand-blue)"/>
      <path d="M0 0 H655 C690 20 640 70 680 133 H0 Z" fill="#6fae6f"/>
      <path d="M0 0 H640 C672 25 625 80 660 133 H0 Z" fill="var(--brand-green)"/>
      <path d="M0 0 H628 C655 30 612 85 648 133 H0 Z" fill="url(#panelGrey)"/>
      <rect x="700" y="0" width="460" height="133" fill="#2a4fa6" role="img" aria-label="Large interlocking puzzle pieces as header decoration"/>
    </svg>
    <div class="brand"><span>Kaltro Energy</span><span class="brand-mark"></span></div>
  </header>

  <nav class="main-nav">
    <a class="major" href="#" style="left:97px">Home</a>
    <a href="#" style="left:184px">About Us</a>
    <a href="#" style="left:277px">Services</a>
    <a href="#" style="left:361px">Projects and Case Studies</a>
    <a class="major" href="#" style="left:551px">Financial Information</a>
    <a href="#" style="left:755px">News</a>
    <a href="#" style="left:825px">Contact</a>
  </nav>

  <main>
    <h1 class="page-title">Resource Efficiency – Sustainable Solutions</h1>
    <div class="intro">
      <p style="top:287px">Is your business performing as<br>well as your competitors?</p>
      <p style="top:375px">Are your fixed costs comparable<br>to industry leaders?</p>
      <p style="top:463px">Is your business becoming less<br>profitable with increased<br>energy, waste and water prices?</p>
      <p style="top:580px">Do you wish to reduce your<br>impact on the environment through reducing the use of resources (energy, waste and water)<br>within your business?</p>
    </div>
    <div class="feature-photo" role="img" aria-label="Photo of a businessman holding up a puzzle piece above the word Solution"></div>
  </main>

  <aside class="sidebar">
    <div class="search">
      <svg width="15" height="15" viewBox="0 0 15 15"><circle cx="6" cy="6" r="4.5" fill="none" stroke="#8a8a8a" stroke-width="2"/><path d="M9.5 9.5 L14 14" stroke="#8a8a8a" stroke-width="2.4"/></svg>
      <span>Search</span>
    </div>
    <h2 class="newsletter-title">Kaltro<br>Energy<br>Newsletter</h2>
    <p class="newsletter-copy">Would you like to receive our regular monthly Newsletter? Please fill in your Name:</p>
    <div class="field"></div>
    <p class="newsletter-copy" style="margin-top:0">Let us know your email address so we can send the Newsletter directly to your email address. (Note that your details will not be passed onto any 3rd</p>
  </aside>
</body>
</html>
```